Create modern and sleek business card for luxury real estate company

We're a "boutique" real estate office looking for a design that gets across a highly modern luxury brand. Blacks and whites are probably the best colors unless we try a silver foil for the logo. I've attached a version of our current logo here. I'd like to swap out the current font on there with Gotham Light Regular.

I'm looking to have one side of the card have the logo with the space for our agents info on the other side.

Target Market(s)

Young professionals in a "luxury" headspace

Industry/Entity Type

Real estate

Contact Information for Business Card

A place for agent name, cell number, website. The slogan "Simply Rethinking Real Estate".

Font styles to use
Other font styles liked:
• Gotham Regular

Colors

Designer to choose only greyscale colors for use in the design.

Requirements
Must have
• Matte black as the background color. Clean lines and use of contrast. A specific design aspect that will use silver foil.
Nice to have
• Up in the air on integrating a QR code
Should not have
• Any houses or other real estate related design (ex: a clip art house)

```html
<!DOCTYPE html>
<html lang="en">
<head>
<meta charset="utf-8">
<title>Halden Realty – Business Card</title>
<link href="https://fonts.googleapis.com/css2?family=Montserrat:wght@300;400;700&family=Dancing+Script:wght@500&display=swap" rel="stylesheet">
<style>
  :root {
    --backdrop: #2b3037;
    --card-black: #1c1a1b;
    --photo-dark: #2a2829;
    --photo-mid: #4a4748;
    --photo-light: #6a6768;
    --divider: #3c3a3b;
    --silver: #c9c9cb;
    --silver-soft: #a9a9ab;
    --white: #ffffff;
  }
  * { margin: 0; padding: 0; box-sizing: border-box; }
  html, body {
    width: 1200px; height: 1200px; overflow: hidden;
    background: var(--backdrop);
  }
  .stage {
    width: 1200px; height: 1200px;
    display: flex; align-items: center; justify-content: center;
  }
  .card {
    width: 1000px; height: 560px;
    display: flex;
    background: var(--card-black);
    font-family: "Montserrat", Arial, sans-serif;
    overflow: hidden;
  }
  .brand-side {
    position: relative;
    width: 600px; height: 100%;
    background:
      linear-gradient(160deg, var(--photo-mid) 0%, var(--photo-dark) 45%, var(--photo-light) 70%, var(--photo-dark) 100%);
  }
  .brand-side__photo { position: absolute; inset: 0; }
  .divider-strip {
    width: 22px; height: 100%;
    background: var(--divider);
  }
  .brand {
    position: absolute; left: 60px; top: 80px;
    display: flex; align-items: center; gap: 28px;
  }
  .brand__circle {
    width: 150px; height: 150px; border-radius: 50%;
    border: 4px solid var(--silver);
    flex: none;
  }
  .brand__name {
    color: var(--silver);
    font-weight: 300;
    font-size: 64px;
    line-height: 1.05;
    letter-spacing: 2px;
    text-transform: uppercase;
  }
  .agent-name {
    position: absolute; left: 230px; top: 330px;
    color: var(--white);
    font-weight: 700;
    font-size: 42px;
  }
  .info-side {
    flex: 1;
    padding: 70px 40px 0 40px;
    display: flex; flex-direction: column;
  }
  .slogan {
    font-family: "Dancing Script", cursive;
    font-weight: 500;
    color: var(--silver-soft);
    font-size: 44px;
    line-height: 1.25;
  }
  .contacts {
    margin-top: 70px;
    display: flex; gap: 18px;
  }
  .contacts__rail { flex: none; }
  .contacts__list {
    list-style: none;
    color: var(--silver);
    font-weight: 400;
    font-size: 22px;
    letter-spacing: 1px;
  }
  .contacts__list li { height: 44px; line-height: 36px; }
  .contacts__list li.web { height: auto; line-height: 1.5; }
</style>
</head>
<body>
<div class="stage">
  <div class="card">
    <div class="brand-side">
      <div class="brand-side__photo" role="img" aria-label="Black and white photograph of towering skyscrapers seen from below"></div>
      <div class="brand">
        <div class="brand__circle"></div>
        <div class="brand__name">Halden<br>Realty</div>
      </div>
      <div class="agent-name">Lorem ipsum</div>
    </div>
    <div class="divider-strip"></div>
    <div class="info-side">
      <p class="slogan">“ Simply Rethinking<br>&nbsp;Real Estate ”</p>
      <div class="contacts">
        <svg class="contacts__rail" width="36" height="124" viewBox="0 0 36 124" fill="none" stroke="#ffffff" stroke-width="2">
          <line x1="18" y1="34" x2="18" y2="46"/>
          <line x1="18" y1="78" x2="18" y2="90"/>
          <circle cx="18" cy="18" r="15"/>
          <path d="M13 11 q-3 7 3 13 q5 4 8 2 l-2-4 -3 1 q-3-3-3-6 l2-2 -2-4z" fill="#ffffff" stroke="none"/>
          <circle cx="18" cy="62" r="15"/>
          <rect x="10" y="56" width="16" height="12" fill="#ffffff" stroke="none"/>
          <path d="M10 56 l8 7 8-7" stroke="#1c1a1b" stroke-width="1.5"/>
          <circle cx="18" cy="106" r="15"/>
          <path d="M18 98 l6 10 h-4 v6 h-4 v-6 h-4z" fill="#ffffff" stroke="none"/>
        </svg>
        <ul class="contacts__list">
          <li>555.014.2290</li>
          <li>Lorem@ipsum.com</li>
          <li class="web">www.Lorem ipsum.com<br>www.Lorem ipsum.com</li>
        </ul>
      </div>
    </div>
  </div>
</div>
</body>
</html>
```